Redesigning the company webpage

we have our website and we are not happy with the current designer. Our main business is dry cleaning through our innovative smart lockers. Customers can place an order online get assigned a locker to drop clothes in. We have the logo, promo video and most of the content. The site is built using WordPress and woo commerce. In addition to the overhaul, some programming is needed to connect the website to Twilio for OTP and order verification.

Target Market(s)

Australia

Industry/Entity Type

Business

Number of Pages Required

5+ page

Font styles to use
Sans Serif

Requirements
Must have
• The website should reflect the innovative nature of the service. Hitech and modern way of drycleaning and laundry
Should not have
• this is not a laundermat shop

```html
<!DOCTYPE html>
<html lang="en">
<head>
<meta charset="utf-8">
<title>SpinVault — 24/7 Dry Cleaning &amp; Laundry</title>
<link href="https://fonts.googleapis.com/css2?family=Open+Sans:wght@400;600;700&family=Lato:ital,wght@0,400;0,700;1,700&display=swap" rel="stylesheet">
<style>
:root{
  --blue:#2f9bc9;
  --blue-dark:#2586b0;
  --navy:#1c3448;
  --hero-top:#5d7184;
  --hero-bot:#31465a;
  --ink:#2b3a44;
  --muted:#7a8790;
  --line:#dfe6ea;
  --white:#ffffff;
  --footer:#9aa6ad;
}
*{margin:0;padding:0;box-sizing:border-box}
html,body{width:1200px;height:2492px;overflow:hidden}
body{font-family:"Open Sans",Arial,sans-serif;color:var(--ink);background:var(--white);position:relative}

/* hero */
.hero{position:absolute;left:0;top:0;width:1200px;height:620px;
  background:linear-gradient(180deg,var(--hero-top),var(--hero-bot));}
.hero-photo{position:absolute;inset:0;
  background:radial-gradient(circle at 180px 330px,rgba(140,160,175,.35) 0 150px,transparent 152px),
             radial-gradient(circle at 1040px 330px,rgba(140,160,175,.35) 0 150px,transparent 152px),
             linear-gradient(180deg,rgba(20,40,60,.1),rgba(20,40,60,.4));}
.brand{position:absolute;left:120px;top:30px;font-family:"Lato",sans-serif;font-weight:700;font-size:26px;letter-spacing:1px;color:var(--white)}
.nav{position:absolute;right:110px;top:24px;display:flex;gap:12px;list-style:none}
.nav li{font-size:13px;font-weight:600;color:var(--white);padding:10px 18px;border-radius:22px}
.nav li.active{background:var(--blue)}
.hero-title{position:absolute;left:0;width:1200px;top:230px;text-align:center;font-family:"Lato",sans-serif;font-size:50px;color:var(--white);font-weight:400}
.hero-title em{font-style:italic;font-weight:700}
.hero-actions{position:absolute;top:300px;left:0;width:1200px;display:flex;justify-content:center;gap:26px}
.btn{width:180px;height:48px;display:flex;align-items:center;justify-content:center;font-size:13px;font-weight:700;color:var(--white);letter-spacing:.5px}
.btn-solid{background:var(--blue)}
.btn-ghost{border:2px solid var(--white)}
.watch{position:absolute;top:404px;left:0;width:1200px;display:flex;justify-content:center;align-items:center;gap:16px;color:var(--white);font-size:14px;font-weight:700}
.watch span{display:block;width:48px;height:48px;border-radius:50%;background:var(--white);position:relative}

/* subscribe */
.subscribe{position:absolute;top:620px;left:0;width:1200px;height:120px;background:var(--blue);color:var(--white)}
.subscribe h3{position:absolute;left:180px;top:28px;font-weight:400;font-size:28px}
.subscribe p{position:absolute;left:180px;top:72px;font-size:13px;opacity:.85}
.subscribe .field{position:absolute;left:480px;top:36px;width:520px;height:52px;background:var(--blue-dark);border:1px solid rgba(255,255,255,.25);font-size:13px;padding:17px 20px;color:rgba(255,255,255,.75)}
.subscribe .join{position:absolute;left:1020px;top:36px;width:150px;height:52px;border:2px solid var(--white);display:flex;align-items:center;justify-content:center;gap:10px;font-weight:700;font-size:15px}

/* steps */
.steps-head{position:absolute;top:830px;left:0;width:1200px;text-align:center}
.steps-head h2{font-family:"Lato",sans-serif;font-size:46px;color:var(--blue);font-weight:700}
.steps-head h4{font-family:"Lato",sans-serif;font-size:28px;font-weight:700;color:var(--ink);margin-top:10px}
.steps{position:absolute;top:1030px;left:160px;width:880px;display:flex;justify-content:space-between}
.step{width:200px;text-align:center;position:relative}
.step .num{width:50px;height:50px;border-radius:50%;background:var(--blue);color:var(--white);font-weight:700;font-size:20px;line-height:50px;margin:0 auto;position:relative;z-index:2}
.step .icon{width:170px;height:170px;border-radius:50%;border:1px solid var(--line);margin:-25px auto 0;display:flex;align-items:center;justify-content:center;background:var(--white)}
.step h5{font-size:16px;font-weight:700;color:var(--blue);margin-top:26px}
.step p{font-size:13px;color:var(--muted);line-height:20px;margin-top:8px}

/* dashboard */
.dash-photo{position:absolute;top:1480px;left:0;width:600px;height:400px;background:linear-gradient(135deg,#8a6a4e,#c9c0b3 55%,#e8e6e2)}
.dash-callout{position:absolute;top:1535px;left:220px;width:370px;height:100px;background:var(--blue);color:var(--white);font-size:19px;font-weight:700;text-align:center;display:flex;align-items:center;justify-content:center;line-height:28px}
.status{position:absolute;top:1520px;left:750px;width:380px;list-style:none}
.status li{display:flex;gap:20px;height:102px}
.status .ring{width:66px;height:66px;border-radius:50%;border:2px solid var(--blue);display:flex;align-items:center;justify-content:center;flex:none}
.status h6{font-size:15px;font-weight:700;color:var(--blue);margin-top:12px}
.status p{font-size:13px;color:var(--muted);margin-top:6px}

/* testimonials */
.testimonials{position:absolute;top:1940px;left:0;width:1200px;height:480px;background:var(--blue)}
.testimonials h2{position:absolute;top:42px;width:1200px;text-align:center;color:var(--white);font-weight:400;font-size:34px}
.quote{position:absolute;top:180px;left:192px;width:908px;height:150px;background:var(--white);padding:26px 40px 0 80px;font-size:13px;line-height:22px;color:var(--muted)}
.quote::after{content:"";position:absolute;left:80px;bottom:-16px;border-left:16px solid transparent;border-right:16px solid transparent;border-top:16px solid var(--white)}
.quote b{position:absolute;left:30px;top:20px;font-family:"Lato",sans-serif;font-size:44px;color:var(--blue);line-height:1}
.avatar{position:absolute;top:350px;left:200px;width:80px;height:80px;border-radius:50%;background:linear-gradient(135deg,#c7b3a0,#6d5a4b);border:3px solid var(--white)}
.person{position:absolute;top:364px;left:300px;color:var(--white)}
.person strong{font-size:17px;display:block}
.person span{font-size:12px;opacity:.85}
.arrows{position:absolute;top:368px;left:1026px;display:flex;gap:10px}
.arrows span{width:34px;height:34px;border-radius:50%;background:var(--white);display:flex;align-items:center;justify-content:center}

/* footer */
.footer{position:absolute;top:2420px;left:0;width:1200px;height:72px;font-size:12px;color:var(--footer)}
.footer p{position:absolute;left:140px;top:28px}
.footer .social{position:absolute;right:140px;top:26px;display:flex;gap:30px}
.footer .social i{width:16px;height:16px;border-radius:50%;background:var(--blue);display:block}
</style>
</head>
<body>

<header class="hero">
  <div class="hero-photo" role="img" aria-label="Photo of a row of front-loading washing machines under a dark blue overlay"></div>
  <div class="brand">SPINVAULT</div>
  <ul class="nav">
    <li class="active">HOME</li><li>ABOUT US</li><li>SERVICES</li><li>FAQ</li><li>CONTACT US</li>
  </ul>
  <h1 class="hero-title"><em>24/7</em> Dry Cleaning &amp; Laundry!</h1>
  <div class="hero-actions">
    <div class="btn btn-solid">REGISTER NOW</div>
    <div class="btn btn-ghost">LEARN MORE</div>
  </div>
  <div class="watch">
    <span><svg width="48" height="48" viewBox="0 0 48 48"><path d="M20 16 L32 24 L20 32Z" fill="#31465a"/></svg></span>
    WATCH VIDEO
  </div>
</header>

<section class="subscribe">
  <h3>Subscribe</h3>
  <p>Join our email list to get future updates</p>
  <div class="field">Your Email Address</div>
  <div class="join">JOIN <svg width="16" height="16" viewBox="0 0 16 16"><path d="M1 8 L15 1 L11 15 L8 9Z" fill="#fff"/></svg></div>
</section>

<section>
  <div class="steps-head">
    <h2>GET YOUR LAUNDRY DONE</h2>
    <h4>WITH 4 SIMPLE STEPS</h4>
  </div>
  <div class="steps">
    <div class="step">
      <div class="num">1</div>
      <div class="icon"><svg width="70" height="60" viewBox="0 0 70 60" fill="none" stroke="#2f9bc9" stroke-width="2"><rect x="10" y="6" width="50" height="34" rx="2"/><path d="M4 46 H66 L62 52 H8Z"/></svg></div>
      <h5>REGISTER</h5>
      <p>register and pay laundry through our website</p>
    </div>
    <div class="step">
      <div class="num">2</div>
      <div class="icon"><svg width="50" height="70" viewBox="0 0 50 70" fill="none" stroke="#2f9bc9" stroke-width="2"><rect x="8" y="4" width="34" height="62" rx="4"/><path d="M8 14H42M8 54H42"/><circle cx="25" cy="60" r="2"/></svg></div>
      <h5>GET PASSWORD</h5>
      <p>we send the password to unlock your locker to your phone</p>
    </div>
    <div class="step">
      <div class="num">3</div>
      <div class="icon"><svg width="56" height="66" viewBox="0 0 56 66" fill="none" stroke="#2f9bc9" stroke-width="2"><rect x="4" y="4" width="48" height="58" rx="3"/><path d="M4 16H52"/><circle cx="28" cy="39" r="15"/><circle cx="12" cy="10" r="2"/></svg></div>
      <h5>LAUNDRY</h5>
      <p>put your laundry to your locker and we will pick and laundry them</p>
    </div>
    <div class="step">
      <div class="num">4</div>
      <div class="icon"><svg width="70" height="60" viewBox="0 0 70 60" fill="none" stroke="#2f9bc9" stroke-width="2"><path d="M24 6 L6 16 L12 28 L18 25 V54 H52 V25 L58 28 L64 16 L46 6 Q35 16 24 6Z"/></svg></div>
      <h5>READY TO PICK UP</h5>
      <p>you can check your laundry status whether it is ready or not</p>
    </div>
  </div>
</section>

<section>
  <div class="dash-photo" role="img" aria-label="Photo of hands typing on a laptop on a wooden desk beside a notepad"></div>
  <div class="dash-callout">CHECK YOUR LAUNDRY STATUS<br>FROM YOUR DASHBOARD</div>
  <ul class="status">
    <li><div class="ring"><svg width="30" height="34" viewBox="0 0 30 34" fill="none" stroke="#2f9bc9" stroke-width="2"><rect x="3" y="2" width="24" height="30"/><path d="M15 2V32"/><path d="M10 16V20M20 16V20"/></svg></div>
      <div><h6>IN LOCKER</h6><p>Your laundry is still in locker, it still waiting to laundry.</p></div></li>
    <li><div class="ring"><svg width="32" height="32" viewBox="0 0 32 32" fill="none" stroke="#2f9bc9" stroke-width="2"><circle cx="16" cy="16" r="6"/><path d="M16 2V7M16 25V30M2 16H7M25 16H30M6 6L9.5 9.5M22.5 22.5L26 26M26 6L22.5 9.5M9.5 22.5L6 26"/></svg></div>
      <div><h6>WORKING ON IT</h6><p>Your laundry is in the process. Wait until its done :)</p></div></li>
    <li><div class="ring"><svg width="30" height="30" viewBox="0 0 30 30" fill="none" stroke="#2f9bc9" stroke-width="3"><path d="M5 16 L12 23 L25 8"/></svg></div>
      <div><h6>READY FOR PICK UP</h6><p>Your laundry is ready for pick up.</p></div></li>
    <li><div class="ring"><svg width="30" height="32" viewBox="0 0 30 32" fill="none" stroke="#2f9bc9" stroke-width="2"><path d="M4 10H26L24 30H6Z"/><path d="M10 10V7A5 5 0 0 1 20 7V10"/></svg></div>
      <div><h6>PICKED UP</h6><p>Your laundry has been picked up.</p></div></li>
  </ul>
</section>

<section class="testimonials">
  <h2>Testimonials</h2>
  <blockquote class="quote"><b>&ldquo;</b>The locker service has made my week so much easier. I drop my shirts off on the way to work, get a code on my phone, and pick everything up fresh and pressed the next evening. No queues, no waiting, and the status updates tell me exactly where my order is. Honestly the most convenient dry cleaning I have used in years.</blockquote>
  <div class="avatar" role="img" aria-label="Customer portrait photo"></div>
  <div class="person"><strong>DR. MARCUS ELLWOOD</strong><span>Regular customer</span></div>
  <div class="arrows">
    <span><svg width="12" height="12" viewBox="0 0 12 12"><path d="M8 1 L3 6 L8 11" fill="none" stroke="#2f9bc9" stroke-width="2"/></svg></span>
    <span><svg width="12" height="12" viewBox="0 0 12 12"><path d="M4 1 L9 6 L4 11" fill="none" stroke="#2f9bc9" stroke-width="2"/></svg></span>
  </div>
</section>

<footer class="footer">
  <p>Copyright © 2024 SpinVault</p>
  <div class="social"><i></i><i></i><i></i></div>
</footer>

</body>
</html>
```